Tincture bottle labels

I need my labels slightly adjusted to replace the ingredients part with the supplement facts as shown in the 3 Velmarine labels attached, for the other 2 it will have to be copied and add an KBR disclosure on the label as well possibly below the storage info near the bottom of the label

Target Market(s)

Everyone

Industry/Entity Type

Vitamins & Supplements

Requirements
Must have
• Supplement facts box and info for each product and KBR disclosures

```html
<!DOCTYPE html>
<html lang="en">
<head>
<meta charset="utf-8">
<title>Velmarine Tincture Labels</title>
<link rel="stylesheet" href="https://fonts.googleapis.com/css2?family=Lilita+One&family=Barlow:ital,wght@1,800&family=Source+Sans+3:wght@400;700;900&display=swap">
<style>
  :root {
    --canvas: #d1d2d4;
    --ink: #111111;
    --paper: #ffffff;
    --brick: #a5472b;
    --brick-dark: #7f331d;
    --toadstool: #e3262d;
  }
  * { box-sizing: border-box; margin: 0; padding: 0; }
  html, body { width: 668px; height: 1200px; overflow: hidden; background: var(--canvas); }
  .sheet { position: relative; width: 668px; height: 1200px; font-family: "Source Sans 3", sans-serif; color: var(--ink); }

  .label {
    position: absolute; left: 68px; width: 532px; height: 200px; overflow: hidden;
    background: linear-gradient(90deg, var(--base) 0%, var(--base2) 100%);
  }
  .label--cordyceps { top: 69px;  --base:#5a3a98; --base2:#6b3f9e; --accent:#1f9ad8; --photo1:#e98b2b; --photo2:#6b4a2a; }
  .label--lions-mane{ top: 284px; --base:#f68b24; --base2:#ef6a22; --accent:#41ad3c; --photo1:#efe4d0; --photo2:#5b5f63; }
  .label--turkey-tail{ top: 500px; --base:#2e9a55; --base2:#2f7a6a; --accent:#f6c519; --photo1:#d98a33; --photo2:#3a2c22; }
  .label--chaga     { top: 715px; --base:#3b8fd6; --base2:#b8e3f8; --accent:#f26d22; --photo1:#8a6a4a; --photo2:#2f3236; }
  .label--reishi    { top: 930px; --base:#9cb2e6; --base2:#4f7fc8; --accent:#e1232b; --photo1:#c4542e; --photo2:#5a2a20; }

  .label__photo { position: absolute; inset: 0; width: 532px; height: 200px; }

  .label__wall {
    position: absolute; left: 0; right: 0; bottom: 0; height: 42px;
    background: linear-gradient(180deg, var(--brick) 0%, var(--brick-dark) 100%);
    border-top: 3px solid var(--accent);
  }

  .toadstool {
    position: absolute; width: 9px; height: 10px; top: 142px;
    background: var(--toadstool); border-radius: 50% 50% 35% 35%;
  }

  .maker {
    position: absolute; left: 20px; top: 22px; height: 140px;
    writing-mode: vertical-rl; color: var(--paper);
    font-size: 4.4px; line-height: 5.4px;
  }
  .maker strong { font-weight: 900; text-transform: uppercase; }
  .maker__site { position: absolute; left: 20px; top: 80px; writing-mode: vertical-rl; color: var(--paper); font-size: 4.6px; }

  .facts {
    position: absolute; left: 47px; top: 19px; width: 88px; height: 152px;
    background: var(--paper); border: 1.5px solid var(--ink); border-radius: 6px;
    box-shadow: 2px 2px 0 var(--ink); padding: 4px 6px;
    font-size: 5.4px; line-height: 6.2px;
  }
  .facts__table { border: 0.8px solid var(--ink); padding: 1.5px 2px; font-size: 3.9px; line-height: 4.6px; }
  .facts__title { font-size: 6.6px; line-height: 7px; font-weight: 700; }
  .facts__row { display: flex; justify-content: space-between; font-weight: 700; border-top: 2px solid var(--ink); border-bottom: 0.6px solid var(--ink); margin-top: 1px; }
  .facts__ingredient { border-bottom: 1.4px solid var(--ink); padding: 0.5px 0; }
  .facts__heading { font-size: 4.6px; line-height: 5px; font-weight: 900; text-transform: uppercase; margin-top: 4px; }

  .disclaimer {
    position: absolute; left: 30px; top: 176px; width: 125px; height: 21px;
    background: var(--paper); border: 0.8px solid var(--ink);
    font-size: 4.3px; line-height: 5.6px; padding: 1px 2px;
  }

  .brand { position: absolute; left: 180px; top: 8px; width: 172px; text-align: center; }
  .brand__dot { display: block; width: 30px; height: 30px; margin: 0 auto 4px; border-radius: 50%; background: var(--accent); }
  .brand__name { font-family: "Lilita One", sans-serif; font-size: 27px; line-height: 30px; color: var(--accent); letter-spacing: 0.5px; }

  .product-name {
    position: absolute; left: 150px; width: 232px; top: 112px; text-align: center;
    font-family: "Lilita One", sans-serif; font-size: 16px; line-height: 18px; letter-spacing: 1px;
    color: var(--paper); text-shadow: 1px 1px 0 #2a2a2a;
  }
  .format-pill {
    position: absolute; left: 217px; top: 146px; width: 97px; height: 23px; border-radius: 12px;
    background: var(--accent); color: var(--paper); text-align: center;
    font-size: 10px; line-height: 23px;
  }
  .volume {
    position: absolute; left: 180px; width: 172px; top: 178px; text-align: center;
    font-family: "Lilita One", sans-serif; font-size: 8.5px; color: var(--paper); letter-spacing: 0.4px;
  }

  .benefits {
    position: absolute; left: 406px; top: 19px; width: 93px; height: 151px;
    background: var(--paper); border: 1.5px solid var(--ink); border-radius: 8px;
    box-shadow: 3px 3px 0 var(--ink); padding: 9px 5px 0;
  }
  .benefits__headline { font-family: "Lilita One", sans-serif; font-size: 9.6px; line-height: 13px; text-align: center; text-transform: uppercase; }
  .benefits__label { font-family: "Lilita One", sans-serif; font-size: 8.6px; text-align: center; margin-top: 9px; text-transform: uppercase; }
  .benefits__list { list-style: none; margin-top: 3px; padding-left: 10px; }
  .benefits__list li {
    position: relative; font-family: "Barlow", sans-serif; font-weight: 800; font-style: italic;
    font-size: 7.4px; line-height: 8px; text-transform: uppercase; margin-bottom: 5px;
  }
  .benefits__list li::before { content: ""; position: absolute; left: -7px; top: 3.5px; width: 2.2px; height: 2.2px; border-radius: 50%; background: var(--ink); }

  .sheet-note { position: absolute; left: 88px; top: 490px; font-size: 5px; font-weight: 700; }
</style>
</head>
<body>
<main class="sheet">

  <!-- Cordyceps -->
  <section class="label label--cordyceps">
    <svg class="label__photo" viewBox="0 0 532 200" role="img" aria-label="Photo of orange cordyceps mushrooms">
      <defs><linearGradient id="photo-cordyceps" x1="0" x2="1" y1="0" y2="1"><stop offset="0" stop-color="#e98b2b"/><stop offset="1" stop-color="#6b4a2a"/></linearGradient></defs>
      <path d="M170 0 C230 0 250 36 310 46 L532 46 L532 0 Z" fill="url(#photo-cordyceps)"/>
    </svg>
    <div class="label__wall" role="img" aria-label="Brick wall pattern"></div>
    <span class="toadstool" style="left:144px" role="img" aria-label="Small toadstool icon"></span>
    <span class="toadstool" style="left:326px" role="img" aria-label="Small toadstool icon"></span>
    <div class="maker"><strong>Manufactured by:</strong><br>Velmarine LLC<br>Harbor City, Easton</div>
    <div class="maker__site">velmarine.shop</div>
    <div class="facts">
      <div class="facts__table">
        <div class="facts__title">Supplement Facts</div>
        <div>Serving Size: 2 droppers (2ML)</div>
        <div>Servings Per Container: About 30</div>
        <div class="facts__row"><span>Amount Per Serving</span><span>2mL*</span></div>
        <div class="facts__ingredient">Organic Cordyceps (Cordyceps Militaris) fruitbody extract</div>
        <div>*Daily value not established</div>
      </div>
      <div class="facts__heading">Other ingredients:</div>
      <div>Spring Water, Cane Alcohol. Alcohol content ~20%</div>
      <div class="facts__heading">Suggested use:</div>
      <div>Take 1-2 ml daily, or as directed by your healthcare provider. Consume directly or add to beverages for a cognitive boost.</div>
      <div class="facts__heading">Storage:</div>
      <div>Store in a cool, dry place away from sunlight.</div>
    </div>
    <div class="disclaimer">These statements have not been evaluated by the KBR. This product is not intended to diagnose, treat, cure, or prevent any disease.</div>
    <div class="brand"><span class="brand__dot"></span><span class="brand__name">VELMARINE</span></div>
    <h2 class="product-name">CORDYCEPS</h2>
    <div class="format-pill">LIQUID DROPS</div>
    <div class="volume">2 fl. oz / (60 ml)</div>
    <div class="benefits">
      <div class="benefits__headline">Boost energy and improve endurance</div>
      <div class="benefits__label">Key benefits:</div>
      <ul class="benefits__list"><li>Enhances energy</li><li>Stamina</li><li>Oxygen utilization</li></ul>
    </div>
  </section>

  <!-- Lion's Mane -->
  <section class="label label--lions-mane">
    <svg class="label__photo" viewBox="0 0 532 200" role="img" aria-label="Photo of white lion's mane mushroom">
      <defs><linearGradient id="photo-lions-mane" x1="0" x2="1" y1="0" y2="0"><stop offset="0" stop-color="#efe4d0"/><stop offset="0.7" stop-color="#d9cbb3"/><stop offset="1" stop-color="#5b5f63"/></linearGradient></defs>
      <path d="M0 0 L0 8 C60 8 120 4 150 6 C220 10 250 60 300 62 L532 62 L532 0 Z" fill="url(#photo-lions-mane)"/>
    </svg>
    <div class="label__wall" role="img" aria-label="Brick wall pattern"></div>
    <span class="toadstool" style="left:16px" role="img" aria-label="Small toadstool icon"></span>
    <span class="toadstool" style="left:144px" role="img" aria-label="Small toadstool icon"></span>
    <span class="toadstool" style="left:326px" role="img" aria-label="Small toadstool icon"></span>
    <div class="maker"><strong>Manufactured by:</strong><br>Velmarine LLC<br>Harbor City, Easton</div>
    <div class="maker__site">velmarine.shop</div>
    <div class="facts">
      <div class="facts__table">
        <div class="facts__title">Supplement Facts</div>
        <div>Serving Size: 2 droppers (2ML)</div>
        <div>Servings Per Container: About 30</div>
        <div class="facts__row"><span>Amount Per Serving</span><span>2mL*</span></div>
        <div class="facts__ingredient">Organic Lion's Mane (Hericium Erinaceus) fruitbody extract</div>
        <div>*Daily value not established</div>
      </div>
      <div class="facts__heading">Other ingredients:</div>
      <div>Spring Water, Cane Alcohol. Alcohol content ~20%</div>
      <div class="facts__heading">Suggested use:</div>
      <div>Take 1-2 ml daily, or as directed by your healthcare provider. Consume directly or add to beverages for a cognitive boost.</div>
      <div class="facts__heading">Storage:</div>
      <div>Store in a cool, dry place away from sunlight.</div>
    </div>
    <div class="disclaimer">These statements have not been evaluated by the KBR. This product is not intended to diagnose, treat, cure, or prevent any disease.</div>
    <div class="brand"><span class="brand__dot"></span><span class="brand__name">VELMARINE</span></div>
    <h2 class="product-name">LION’S MANE</h2>
    <div class="format-pill">LIQUID DROPS</div>
    <div class="volume">2 fl. oz / (60 ml)</div>
    <div class="benefits">
      <div class="benefits__headline">Enhance memory, focus, &amp; nerve health</div>
      <div class="benefits__label">Key benefits:</div>
      <ul class="benefits__list"><li>Supports brain health</li><li>Cognitive function</li><li>Nerve regeneration</li></ul>
    </div>
  </section>

  <div class="sheet-note">Trametes Versicolor</div>

  <!-- Turkey Tail -->
  <section class="label label--turkey-tail">
    <svg class="label__photo" viewBox="0 0 532 200" role="img" aria-label="Photo of turkey tail mushrooms on wood">
      <defs><linearGradient id="photo-turkey-tail" x1="0" x2="1" y1="0" y2="1"><stop offset="0" stop-color="#3a2c22"/><stop offset="0.5" stop-color="#d98a33"/><stop offset="1" stop-color="#6a4a2c"/></linearGradient></defs>
      <path d="M0 0 L0 6 C80 6 120 2 160 4 C230 8 250 60 300 64 L532 64 L532 0 Z" fill="url(#photo-turkey-tail)"/>
    </svg>
    <div class="label__wall" role="img" aria-label="Brick wall pattern"></div>
    <span class="toadstool" style="left:144px" role="img" aria-label="Small toadstool icon"></span>
    <span class="toadstool" style="left:326px" role="img" aria-label="Small toadstool icon"></span>
    <div class="maker"><strong>Manufactured by:</strong><br>Velmarine LLC<br>Harbor City, Easton</div>
    <div class="maker__site">velmarine.shop</div>
    <div class="facts">
      <div class="facts__table">
        <div class="facts__title">Supplement Facts</div>
        <div>Serving Size: 2 droppers (2ML)</div>
        <div>Servings Per Container: About 30</div>
        <div class="facts__row"><span>Amount Per Serving</span><span>2mL*</span></div>
        <div class="facts__ingredient">Organic Turkey Tail (Trametes Versicolor) fruitbody extract</div>
        <div>*Daily value not established</div>
      </div>
      <div class="facts__heading">Other ingredients:</div>
      <div>Spring Water, Cane Alcohol. Alcohol content ~20%</div>
      <div class="facts__heading">Suggested use:</div>
      <div>Take 1-2 ml daily, or as directed by your healthcare provider. Consume directly or add to beverages for a cognitive boost.</div>
      <div class="facts__heading">Storage:</div>
      <div>Store in a cool, dry place away from sunlight.</div>
    </div>
    <div class="disclaimer">These statements have not been evaluated by the KBR. This product is not intended to diagnose, treat, cure, or prevent any disease.</div>
    <div class="brand"><span class="brand__dot"></span><span class="brand__name">VELMARINE</span></div>
    <h2 class="product-name">TURKEY TAIL</h2>
    <div class="format-pill">LIQUID DROPS</div>
    <div class="volume">2 fl. oz / (60 ml)</div>
    <div class="benefits">
      <div class="benefits__headline">Nourish your gut &amp; strengthen immunity</div>
      <div class="benefits__label">Key benefits:</div>
      <ul class="benefits__list"><li>Supports digestive health</li><li>Immune system balance</li></ul>
    </div>
  </section>

  <!-- Chaga -->
  <section class="label label--chaga">
    <svg class="label__photo" viewBox="0 0 532 200" role="img" aria-label="Photo of dark chaga fungus on bark">
      <defs><linearGradient id="photo-chaga" x1="0" x2="1" y1="0" y2="0"><stop offset="0" stop-color="#2f3236"/><stop offset="0.5" stop-color="#8a6a4a"/><stop offset="1" stop-color="#3a3a3c"/></linearGradient></defs>
      <path d="M0 0 L0 6 C80 6 120 2 160 4 C230 8 250 60 300 64 L532 64 L532 0 Z" fill="url(#photo-chaga)"/>
    </svg>
    <div class="label__wall" role="img" aria-label="Brick wall pattern"></div>
    <span class="toadstool" style="left:144px" role="img" aria-label="Small toadstool icon"></span>
    <span class="toadstool" style="left:326px" role="img" aria-label="Small toadstool icon"></span>
    <div class="maker"><strong>Manufactured by:</strong><br>Velmarine LLC<br>Harbor City, Easton</div>
    <div class="maker__site">velmarine.shop</div>
    <div class="facts">
      <div class="facts__table">
        <div class="facts__title">Supplement Facts</div>
        <div>Serving Size: 2 droppers (2ML)</div>
        <div>Servings Per Container: About 30</div>
        <div class="facts__row"><span>Amount Per Serving</span><span>2mL*</span></div>
        <div class="facts__ingredient">Organic Chaga (Inonotus Obliquus) fruitbody extract</div>
        <div>*Daily value not established</div>
      </div>
      <div class="facts__heading">Other ingredients:</div>
      <div>Spring Water, Cane Alcohol. Alcohol content ~20%</div>
      <div class="facts__heading">Suggested use:</div>
      <div>Take 1-2 ml daily, or as directed by your healthcare provider. Consume directly or add to beverages for a cognitive boost.</div>
      <div class="facts__heading">Storage:</div>
      <div>Store in a cool, dry place away from sunlight.</div>
    </div>
    <div class="disclaimer">These statements have not been evaluated by the KBR. This product is not intended to diagnose, treat, cure, or prevent any disease.</div>
    <div class="brand"><span class="brand__dot"></span><span class="brand__name">VELMARINE</span></div>
    <h2 class="product-name">CHAGA</h2>
    <div class="format-pill">LIQUID DROPS</div>
    <div class="volume">2 fl. oz / (60 ml)</div>
    <div class="benefits">
      <div class="benefits__headline">Protect and rejuvenate your body</div>
      <div class="benefits__label" style="margin-top:16px">Key benefits:</div>
      <ul class="benefits__list"><li>Antioxidant-rich for anti-aging</li><li>Immune support</li></ul>
    </div>
  </section>

  <!-- Reishi -->
  <section class="label label--reishi">
    <svg class="label__photo" viewBox="0 0 532 200" role="img" aria-label="Photo of glossy red reishi mushroom">
      <defs><linearGradient id="photo-reishi" x1="0" x2="1" y1="0" y2="0"><stop offset="0" stop-color="#c4542e"/><stop offset="0.6" stop-color="#9a4a3a"/><stop offset="1" stop-color="#5a2a20"/></linearGradient></defs>
      <path d="M0 0 L0 6 C80 6 120 2 160 4 C230 8 250 40 300 44 L532 44 L532 0 Z" fill="url(#photo-reishi)"/>
    </svg>
    <div class="label__wall" role="img" aria-label="Brick wall pattern"></div>
    <span class="toadstool" style="left:144px" role="img" aria-label="Small toadstool icon"></span>
    <span class="toadstool" style="left:326px" role="img" aria-label="Small toadstool icon"></span>
    <div class="maker"><strong>Manufactured by:</strong><br>Velmarine LLC<br>Harbor City, Easton</div>
    <div class="maker__site">velmarine.shop</div>
    <div class="facts">
      <div class="facts__table">
        <div class="facts__title">Supplement Facts</div>
        <div>Serving Size: 2 droppers (2ML)</div>
        <div>Servings Per Container: About 30</div>
        <div class="facts__row"><span>Amount Per Serving</span><span>2mL*</span></div>
        <div class="facts__ingredient">Organic Reishi (Ganoderma Lucidum) fruitbody extract</div>
        <div>*Daily value not established</div>
      </div>
      <div class="facts__heading">Other ingredients:</div>
      <div>Spring Water, Cane Alcohol. Alcohol content ~20%</div>
      <div class="facts__heading">Suggested use:</div>
      <div>Take 1-2 ml daily, or as directed by your healthcare provider. Consume directly or add to beverages for a cognitive boost.</div>
      <div class="facts__heading">Storage:</div>
      <div>Store in a cool, dry place away from sunlight.</div>
    </div>
    <div class="disclaimer">These statements have not been evaluated by the KBR. This product is not intended to diagnose, treat, cure, or prevent any disease.</div>
    <div class="brand"><span class="brand__dot"></span><span class="brand__name">VELMARINE</span></div>
    <h2 class="product-name">REISHI</h2>
    <div class="format-pill">LIQUID DROPS</div>
    <div class="volume">2 fl. oz / (60 ml)</div>
    <div class="benefits">
      <div class="benefits__headline">Calm your mind &amp; fortify your immune system</div>
      <div class="benefits__label">Key benefits:</div>
      <ul class="benefits__list"><li>Supports immunity</li><li>Stress reduction</li><li>Overall wellness</li></ul>
    </div>
  </section>

</main>
</body>
</html>
```